Business Cards for Retail/Sourcing Business.

We need a business cards for our company where it looks like:
TK
LM

VERTICAL, where the TK is over the LM. Then Under the TKLM would be name, address and website address. We want the P to be in the style of our original logo, which I uploaded.

Also, can we get a couple of designs with fun colors - especially for the letter head.

Target Market(s)

Old clients. Many of our clients or people we do business with are 40-50 plus. We are not an industry with many young people.

Industry/Entity Type

Business

Contact Information for Business Card

Front side is just says TKLM with name, title, address, and website below.

Font styles to use
Serif
Sans Serif
Decorative
Script

Requirements
Must have
• THE TKLM design with the P in the design of the logo
Nice to have
• Fun colors, new takes on the TKLM and any other additions that would be cool and make it pop

```html
<!DOCTYPE html>
<html lang="en">
<head>
<meta charset="utf-8">
<title>TKLM Business Card</title>
<link href="https://fonts.googleapis.com/css2?family=Montserrat:wght@500;700&family=PT+Sans+Narrow&family=Saira+Semi+Condensed:ital,wght@0,600;1,600&display=swap" rel="stylesheet">
<style>
  :root {
    --backdrop: #e3dfdf;
    --paper: #ffffff;
    --ink: #000000;
    --accent: #e52421;
    --light-text: #ffffff;
  }
  * { margin: 0; padding: 0; box-sizing: border-box; }
  html, body {
    width: 1200px;
    height: 1000px;
    overflow: hidden;
    background: var(--backdrop);
  }
  .card {
    position: absolute;
    left: 476px;
    top: 230px;
    width: 289px;
    height: 479px;
    background: var(--ink);
  }
  .card__brand {
    position: absolute;
    left: 0; top: 0;
    width: 100%;
    height: 223px;
    background: var(--paper);
  }
  .brand-name {
    position: absolute;
    left: 0; top: 26px;
    width: 100%;
    text-align: center;
    font-family: "Montserrat", sans-serif;
    font-weight: 700;
    font-size: 80px;
    line-height: 80px;
    letter-spacing: 2px;
    color: var(--ink);
  }
  .brand-dot {
    position: absolute;
    left: 226px;
    top: 48px;
    width: 16px;
    height: 16px;
    border-radius: 50%;
    background: var(--accent);
  }
  .card__rule {
    position: absolute;
    left: 0; top: 223px;
    width: 100%;
    height: 7px;
    background: var(--accent);
  }
  .holder {
    position: absolute;
    left: 0; top: 270px;
    width: 100%;
    text-align: center;
  }
  .holder__name {
    font-family: "Saira Semi Condensed", sans-serif;
    font-style: italic;
    font-weight: 600;
    font-size: 20px;
    letter-spacing: 1px;
    color: var(--accent);
    line-height: 24px;
  }
  .holder__title {
    margin-top: 4px;
    font-family: "PT Sans Narrow", sans-serif;
    font-size: 14px;
    color: var(--light-text);
  }
  .contact {
    position: absolute;
    left: 54px;
    top: 372px;
    font-family: "Montserrat", sans-serif;
    font-weight: 500;
    font-size: 13px;
    line-height: 15px;
    color: var(--light-text);
  }
  .contact__web {
    display: flex;
    align-items: center;
    gap: 5px;
    margin-bottom: 11px;
  }
  .contact__web svg { width: 11px; height: 11px; }
</style>
</head>
<body>
  <div class="card">
    <div class="card__brand">
      <div class="brand-name">TK<br>LM</div>
      <span class="brand-dot"></span>
    </div>
    <div class="card__rule"></div>
    <div class="holder">
      <div class="holder__name">MARLO BRENNT</div>
      <div class="holder__title">Home Sourcing</div>
    </div>
    <div class="contact">
      <div class="contact__web">
        <svg viewBox="0 0 12 12" aria-hidden="true">
          <circle cx="6" cy="6" r="5" fill="none" stroke="#fff" stroke-width="1.2"/>
          <ellipse cx="6" cy="6" rx="2.2" ry="5" fill="none" stroke="#fff" stroke-width="1"/>
          <line x1="1" y1="6" x2="11" y2="6" stroke="#fff" stroke-width="1"/>
        </svg>
        <span>www.websitedomain.com</span>
      </div>
      <div class="contact__address">000 Harbour Line Road<br>Area Name, NSW, 0000</div>
    </div>
  </div>
</body>
</html>
```